Poster design for Non-Profit Harbor Pathways

Harbor Pathways is a not-for-profit providing disability services to improve the lives of the people we serve. We are holding an internal convention with staff focusing on improving what we already do well. The title of the event and ongoing effort will be ‘Ventus Aperta’, with a sub-title of ‘Focusing on our Strengths’.

Target Market(s)

Our employees

Industry/Entity Type

Non Profit

Font styles to use
Serif

Requirements
Must have
• • Be A0 size
• • Include the title ‘Ventus Aperta’
• • Include the sub-title ‘ Focusing on our Strengths’
• • Include the Harbor Pathways Logo
• • A colour scheme that ties in to our logo
Nice to have
• A bold, minimalist design with clear lettering. Refer to the files inspiration 1 and 2. Also I will upload a brochure we had designed recently. Please ignore our website for design features as it is outdated.
Should not have
• Too many photos.

```html
<!DOCTYPE html>
<html lang="en">
<head>
<meta charset="utf-8">
<title>Ventus Aperta – Focusing on our Strengths</title>
<link rel="stylesheet" href="https://fonts.googleapis.com/css2?family=Bebas+Neue&family=Exo+2:ital,wght@0,600;1,800&display=swap">
<style>
  :root {
    --violet-deep: #5a1a9e;
    --violet: #8a34c8;
    --magenta: #c14fd8;
    --pink-glow: #f2a7ef;
    --white: #ffffff;
    --logo-grey: #e9e4f2;
  }
  * { margin: 0; padding: 0; box-sizing: border-box; }
  html, body { width: 849px; height: 1200px; overflow: hidden; background: var(--violet-deep); }

  .poster {
    position: relative;
    width: 849px;
    height: 1200px;
    overflow: hidden;
    background:
      radial-gradient(ellipse 60% 30% at 75% 85%, rgba(255,220,255,0.55), transparent 70%),
      radial-gradient(ellipse 50% 25% at 15% 78%, rgba(255,200,250,0.35), transparent 70%),
      radial-gradient(ellipse 70% 40% at 50% 45%, rgba(210,110,230,0.45), transparent 75%),
      linear-gradient(180deg, var(--violet-deep) 0%, var(--violet) 40%, var(--magenta) 75%, #d77fe0 100%);
  }

  .light-field {
    position: absolute;
    left: 0; bottom: 0;
    width: 100%; height: 45%;
    background:
      radial-gradient(circle at 20% 60%, rgba(255,255,255,0.25), transparent 18%),
      radial-gradient(circle at 85% 40%, rgba(255,255,255,0.3), transparent 20%),
      radial-gradient(circle at 60% 85%, rgba(255,240,255,0.35), transparent 22%);
  }

  .event-title {
    position: absolute;
    top: 100px;
    width: 100%;
    text-align: center;
    font-family: "Exo 2", sans-serif;
    font-style: italic;
    font-weight: 800;
    font-size: 112px;
    line-height: 1.02;
    letter-spacing: 2px;
    text-transform: uppercase;
    color: var(--violet);
    -webkit-text-stroke: 5px var(--white);
    paint-order: stroke fill;
    text-shadow: 0 0 18px rgba(255,255,255,0.55);
  }

  .rule {
    position: absolute;
    left: 62px;
    width: 725px;
    height: 3px;
    background: var(--white);
    box-shadow: 0 0 10px rgba(255,255,255,0.8);
  }
  .rule--top { top: 428px; }
  .rule--bottom { top: 898px; }

  .event-subtitle {
    position: absolute;
    top: 462px;
    width: 100%;
    text-align: center;
    font-family: "Bebas Neue", sans-serif;
    font-size: 158px;
    line-height: 0.78;
    letter-spacing: 3px;
    color: var(--white);
    text-transform: uppercase;
    text-shadow: 0 0 14px rgba(255,255,255,0.35);
  }

  .organisation {
    position: absolute;
    top: 960px;
    left: 0;
    width: 100%;
    display: flex;
    justify-content: center;
    align-items: center;
    gap: 22px;
  }
  .organisation-mark {
    width: 64px; height: 64px;
    border-radius: 50%;
    background: var(--logo-grey);
  }
  .organisation-name {
    font-family: "Exo 2", sans-serif;
    font-weight: 600;
    font-size: 58px;
    line-height: 1;
    letter-spacing: 1px;
    color: var(--logo-grey);
    text-transform: uppercase;
  }
</style>
</head>
<body>
  <main class="poster">
    <div class="light-field" role="img" aria-label="Soft glowing bokeh lights"></div>

    <h1 class="event-title">Ventus<br>Aperta</h1>

    <div class="rule rule--top"></div>
    <h2 class="event-subtitle">Focusing<br>on our<br>Strengths</h2>
    <div class="rule rule--bottom"></div>

    <div class="organisation">
      <span class="organisation-mark"></span>
      <span class="organisation-name">Harbor Pathways</span>
    </div>
  </main>
</body>
</html>
```